Simple, Professional and neat business card design for Vendralo Inc.

We're looking to re-vamp our business card design. We're a supplier of innovative feed ingredients for the North American animal agriculture industry. We are located in Lucknow, Ontario, Canada and our flagship product is a product that prevents milk fever in dairy cows when the calve, it is fed before calving and is very effective compared to other alternatives available on the market today.

Our company has Danish roots and we import all of our product from our Danish partner/manufacturer in Denmark. We like our design to embrace high professionalism while remaining neat and simple.

Target Market(s)

B2B, Feed Mills, Veterinary Clinics, Large integrators/producers,

Industry/Entity Type

Agribusiness

Contact Information for Business Card

We like the rounded corners because they make the card easy to sit in a wallet and not many use it so it makes the card stand out, just possibly something to take account for during the design.

As you can also see on the sliders below, looking for a that simple but proffesional scandinavian design.

Requirements
Nice to have
• Rounded corners
Should not have
• Too vibrant

```html
<!DOCTYPE html>
<html lang="en">
<head>
<meta charset="utf-8">
<title>Vendralo Inc. business card</title>
<link rel="stylesheet" href="https://fonts.googleapis.com/css2?family=Open+Sans:wght@400;600;700;800&display=swap">
<style>
  :root {
    --brand-blue: #1f63ac;
    --brand-blue-dark: #184f8c;
    --ink: #1d1d1f;
    --card-white: #ffffff;
    --stripe-white: #eef2f7;
    --page: #e6e8eb;
  }
  * { margin: 0; padding: 0; box-sizing: border-box; }
  html, body { width: 1200px; height: 997px; overflow: hidden; }
  body {
    background: var(--page);
    font-family: "Open Sans", Arial, sans-serif;
    position: relative;
  }
  .card {
    position: absolute;
    left: 250px;
    width: 700px;
    height: 400px;
    border-radius: 28px;
    overflow: hidden;
    box-shadow: 0 10px 30px rgba(0,0,0,0.18);
  }

  /* Front: blue side */
  .card-front { top: 70px; background: var(--brand-blue); }
  .front-stripe {
    position: absolute; left: 0; right: 0; top: 300px; height: 58px;
    background: var(--stripe-white);
  }
  .front-brand {
    position: absolute; left: 70px; top: 180px;
    display: flex; align-items: center; gap: 28px;
  }
  .brand-dot {
    width: 74px; height: 74px; border-radius: 50%;
    background: var(--stripe-white);
  }
  .front-name {
    color: var(--card-white);
    font-weight: 800; font-size: 60px; letter-spacing: 1px;
    line-height: 1;
  }
  .front-url {
    position: absolute; left: 0; right: 0; top: 300px; height: 58px;
    display: flex; align-items: center; justify-content: center;
    color: var(--brand-blue); font-weight: 700; font-size: 20px; letter-spacing: 4px;
  }

  /* Back: white side */
  .card-back { top: 530px; background: var(--card-white); }
  .back-brand {
    position: absolute; left: 50px; top: 0; bottom: 0; width: 270px;
    display: flex; flex-direction: column; align-items: center; justify-content: center; gap: 18px;
  }
  .back-brand .brand-dot { width: 110px; height: 110px; background: var(--brand-blue); }
  .back-name {
    color: var(--brand-blue); font-weight: 800; font-size: 30px; letter-spacing: 0.5px;
  }
  .contact {
    position: absolute; left: 360px; top: 62px; width: 300px;
  }
  .contact-rule { height: 2px; background: var(--brand-blue); margin-bottom: 14px; }
  .person-name { color: var(--brand-blue); font-weight: 700; font-size: 18px; letter-spacing: 0.5px; }
  .person-title { color: var(--ink); font-size: 13px; margin-bottom: 16px; }
  .address { color: var(--brand-blue); font-size: 15px; line-height: 1.35; margin-bottom: 16px; }
  .contact-list { list-style: none; margin-left: 28px; }
  .contact-list li {
    display: flex; align-items: center; gap: 10px;
    color: var(--ink); font-size: 16px; line-height: 1; margin-bottom: 9px;
  }
  .icon {
    width: 18px; height: 18px; border-radius: 50%;
    background: var(--brand-blue);
    display: flex; align-items: center; justify-content: center; flex: none;
  }
  .icon svg { width: 11px; height: 11px; fill: var(--card-white); }
</style>
</head>
<body>

<section class="card card-front">
  <div class="front-stripe"></div>
  <div class="front-brand">
    <span class="brand-dot"></span>
    <span class="front-name">VENDRALO INC.</span>
  </div>
  <div class="front-url">www.vendralo.com</div>
</section>

<section class="card card-back">
  <div class="back-brand">
    <span class="brand-dot"></span>
    <span class="back-name">Vendralo Inc.</span>
  </div>
  <div class="contact">
    <div class="contact-rule"></div>
    <p class="person-name">HENRIK MADSEN</p>
    <p class="person-title">Managing Director</p>
    <p class="address">Box 420, Elmwood, Ontario Canada<br>N0G 3K1</p>
    <ul class="contact-list">
      <li><span class="icon"><svg viewBox="0 0 24 24"><path d="M6.6 10.8a15 15 0 0 0 6.6 6.6l2.2-2.2c.3-.3.7-.4 1-.2 1.1.4 2.3.6 3.6.6.6 0 1 .4 1 1V20c0 .6-.4 1-1 1A17 17 0 0 1 3 4c0-.6.4-1 1-1h3.5c.6 0 1 .4 1 1 0 1.3.2 2.5.6 3.6.1.3 0 .7-.2 1z"/></svg></span>555-301-0142</li>
      <li><span class="icon"><svg viewBox="0 0 24 24"><path d="M6.6 10.8a15 15 0 0 0 6.6 6.6l2.2-2.2c.3-.3.7-.4 1-.2 1.1.4 2.3.6 3.6.6.6 0 1 .4 1 1V20c0 .6-.4 1-1 1A17 17 0 0 1 3 4c0-.6.4-1 1-1h3.5c.6 0 1 .4 1 1 0 1.3.2 2.5.6 3.6.1.3 0 .7-.2 1z"/></svg></span>555-301-0187</li>
      <li><span class="icon"><svg viewBox="0 0 24 24"><path d="M4 8h16v10H4zM7 4h10v3H7zM7 13h10v6H7z"/></svg></span>555-301-0199</li>
      <li><span class="icon"><svg viewBox="0 0 24 24"><path d="M6.6 10.8a15 15 0 0 0 6.6 6.6l2.2-2.2c.3-.3.7-.4 1-.2 1.1.4 2.3.6 3.6.6.6 0 1 .4 1 1V20c0 .6-.4 1-1 1A17 17 0 0 1 3 4c0-.6.4-1 1-1h3.5c.6 0 1 .4 1 1 0 1.3.2 2.5.6 3.6.1.3 0 .7-.2 1z"/></svg></span>800-555-0164</li>
      <li><span class="icon"><svg viewBox="0 0 24 24"><path d="M3 5h18v14H3zm2 2v.5l7 5 7-5V7z"/></svg></span>henrik@vendralo.com</li>
    </ul>
  </div>
</section>

</body>
</html>
```